Electrical Contracting Business Website

Require website done for my contracting business.
Partly done one but really dont have time.

You can view the current one at http://tolbran.net.au

You can use any info/styles/photos from the current website

I like the orange color of the logo so id like things to be with that
Unfortunatly being a new business (Sept 2015) I havent got alot of photos . but if you require any for any of the specifics listed in the doc file ill have a look to see what I have.

I am targeting mainly commercial / industrial clients. Which also includes government and mining.

Target Market(s)

People requiring electricians

Industry/Entity Type

Electrician

Coding

Coded - Design and coding required

Number of Pages Required

5+ page

Colors
f37122

Requirements
Must have
• logo with EC Number
• Keep it simple and not to complicated
• Comply with the current html / style sheet standards.
• Desktop/Mobile Version compatability
Nice to have
• additional photos.
• The domestic lifts we install are by vonrim I dont have any photos of them unfortunately.
Should not have
• change colour of logo

```html
<!DOCTYPE html>
<html lang="en">
<head>
<meta charset="utf-8">
<title>Tolbran Engineering</title>
<link href="https://fonts.googleapis.com/css2?family=Roboto:wght@300;400;500;700&display=swap" rel="stylesheet">
<style>
:root{
  --orange:#f15a2b;
  --orange-dark:#e14b1d;
  --orange-deep:#d9441a;
  --grey-bg:#efefef;
  --text-grey:#8f8f8f;
  --text-dark:#3a3a3a;
  --white:#ffffff;
  --field-border:#cfcfcf;
}
*{margin:0;padding:0;box-sizing:border-box}
html,body{width:1200px;height:2778px;overflow:hidden}
body{font-family:'Roboto',Arial,sans-serif;background:var(--white);color:var(--text-dark);position:relative}
section,header,footer{position:absolute;left:0;width:1200px}

/* Hero */
.hero{top:0;height:615px;background:linear-gradient(160deg,#d9d9d9 0%,#c7ced4 35%,#b9c4cc 60%,#d4d4d2 100%)}
.hero-photo{position:absolute;inset:0;background:radial-gradient(ellipse at 70% 55%,rgba(120,160,190,.35),transparent 60%),radial-gradient(ellipse at 20% 25%,rgba(230,200,180,.45),transparent 55%)}
.main-nav{position:absolute;top:30px;left:0;width:1200px;display:flex;justify-content:center;gap:8px}
.main-nav a{font-size:17px;color:#222;text-decoration:none;padding:12px 20px;border-radius:24px;letter-spacing:.2px}
.main-nav a.active{background:var(--orange);color:var(--white)}
.brand{position:absolute;top:250px;left:0;width:1200px;display:flex;justify-content:center;align-items:center;gap:22px}
.brand-dot{width:120px;height:120px;border-radius:50%;background:var(--orange)}
.brand-name{font-size:78px;font-weight:700;color:var(--orange);letter-spacing:1px;line-height:1}
.brand-sub{display:block;font-size:34px;letter-spacing:6px;margin-top:4px}
.hero-ids{position:absolute;top:412px;left:494px;font-size:20px;font-weight:500;color:var(--orange);line-height:28px}
.hero-ids span{margin-left:64px}

/* Values */
.values{top:615px;height:417px}
.values-band{position:absolute;top:0;left:0;width:1200px;height:178px;background:var(--orange)}
.value{position:absolute;top:0;width:272px;height:417px;text-align:center}
.value .head{height:178px;padding-top:36px;color:var(--white)}
.value h3{font-size:21px;font-weight:400;margin-top:16px}
.value p{font-size:15px;line-height:23px;color:var(--text-grey);padding:30px 30px 0}
.value.featured{background:var(--white);box-shadow:0 0 22px rgba(0,0,0,.12)}
.value.featured .head{background:var(--orange-dark);position:relative}
.value.featured .head::after{content:"";position:absolute;left:50%;bottom:-22px;margin-left:-24px;border-left:24px solid transparent;border-right:24px solid transparent;border-top:22px solid var(--orange-dark)}
.value.featured p{padding-top:38px}

/* Welcome */
.welcome{top:1032px;height:453px;background:var(--grey-bg)}
.welcome h2{position:absolute;top:60px;left:80px;font-size:40px;font-weight:400;color:var(--orange)}
.welcome .intro{position:absolute;top:128px;left:80px;width:860px;font-size:15px;line-height:26px;color:var(--text-grey)}
.sectors{position:absolute;top:222px;left:80px;width:740px;height:200px;display:flex}
.sectors::before,.sectors::after{content:"";position:absolute;left:0;width:740px;height:2px;background:linear-gradient(90deg,transparent,#d6d6d6,transparent)}
.sectors::before{top:30px}.sectors::after{bottom:20px}
.sector{flex:1;text-align:center;padding-top:66px;font-size:19px;color:#444;position:relative}
.sector+.sector{border-left:2px solid #dcdcdc}
.sector svg{display:block;margin:0 auto 16px}
.person-photo{position:absolute;right:0;top:6px;width:230px;height:447px;background:linear-gradient(180deg,#d8d0c8 0%,#8e9196 35%,#7b7f86 70%,#5a6c86 100%);border-radius:90px 90px 0 0}

/* About band */
.about-band{top:1485px;height:158px;background:var(--orange);color:var(--white)}
.about-band h2{position:absolute;top:40px;left:80px;font-size:30px;font-weight:400}
.about-band p{position:absolute;top:84px;left:80px;width:760px;font-size:15px;line-height:24px}
.member-badge{position:absolute;top:34px;left:860px;width:260px;height:94px;border:2px solid rgba(255,255,255,.7);border-radius:6px;background:rgba(255,255,255,.12)}

/* Projects */
.projects{top:1643px;height:357px;background:var(--white)}
.projects h2{position:absolute;top:60px;left:0;width:1200px;text-align:center;font-size:41px;font-weight:400;color:var(--orange)}
.project{position:absolute;top:138px;width:500px}
.project-photo{position:absolute;left:0;top:0;width:208px;height:156px;box-shadow:0 12px 14px -10px rgba(0,0,0,.5)}
.project-photo.panel-a{background:linear-gradient(135deg,#2c3544,#5b6a80 50%,#232a36)}
.project-photo.panel-b{background:linear-gradient(135deg,#6b4a1e,#c88a2c 50%,#3d5a3a)}
.project-info{position:absolute;left:228px;top:0;width:270px}
.project-info h3{font-size:21px;font-weight:400;color:var(--orange)}
.project-info .desc{font-size:15px;line-height:22px;color:#555;margin-top:8px}
.project-info dl{display:grid;grid-template-columns:92px 1fr;margin-top:6px;font-size:15px}
.project-info dt{color:var(--orange);font-size:18px}
.project-info dd{color:var(--text-grey);line-height:22px;padding-top:2px}
.project-info dd::before{content:":";color:#555;margin-right:14px;margin-left:-18px}

/* Contact */
.contact{top:2000px;height:474px;background:var(--grey-bg)}
.contact h2{position:absolute;top:58px;left:0;width:1200px;text-align:center;font-size:41px;font-weight:400;color:var(--orange)}
.contact .lead{position:absolute;top:116px;left:175px;width:850px;text-align:center;font-size:15px;line-height:25px;color:#666}
.field{position:absolute;background:var(--white);border:1px solid var(--field-border);font-size:16px;color:#777;padding:14px 12px}
.submit{position:absolute;left:517px;top:356px;width:166px;height:56px;background:var(--orange);color:var(--white);font-size:21px;display:flex;align-items:center;justify-content:center;border:1px solid var(--orange-deep)}

/* Footer */
.site-footer{top:2474px;height:241px;background:var(--orange);color:var(--white)}
.footer-brand{position:absolute;top:78px;left:78px;display:flex;align-items:center;gap:12px}
.footer-brand .brand-dot{width:58px;height:58px;background:var(--white)}
.footer-brand .name{font-size:38px;font-weight:700;line-height:1}
.footer-brand .ids{position:absolute;top:66px;left:70px;font-size:9px;font-weight:700;white-space:nowrap;line-height:12px}
.footer-col{position:absolute;top:38px}
.footer-col h4{font-size:16px;font-weight:500;margin-bottom:12px}
.links li{list-style:none;font-size:15px;line-height:23px;padding-left:18px;position:relative}
.links li::before{content:"»";position:absolute;left:0}
.touch .row{display:flex;gap:18px;font-size:15px;line-height:20px;margin-bottom:16px;align-items:flex-start}
.touch .row svg{flex:none;margin-top:1px}
.touch strong{font-weight:500}
.newsletter p{font-size:15px;line-height:25px;width:255px}
.subscribe{margin-top:18px;width:250px;height:56px;border:1px solid var(--white);display:flex}
.subscribe span{flex:1;font-size:14px;padding:19px 14px}
.subscribe i{width:56px;background:var(--white);display:flex;align-items:center;justify-content:center}
.bottom-bar{top:2715px;height:63px;background:var(--orange-deep);color:#2b1a12;font-size:15px;text-align:center;line-height:63px}
.bottom-bar b{color:var(--white);font-weight:400}
</style>
</head>
<body>

<header class="hero">
  <div class="hero-photo" role="img" aria-label="Photo of a hand testing wiring in an electrical switchboard"></div>
  <nav class="main-nav">
    <a class="active">HOME</a><a>RESIDENTIAL</a><a>COMMERCIAL</a><a>INDUSTRIAL</a><a>ABOUT US</a><a>CONTACT US</a>
  </nav>
  <div class="brand">
    <div class="brand-dot"></div>
    <div class="brand-name">TOLBRAN<span class="brand-sub">ENGINEERING</span></div>
  </div>
  <div class="hero-ids">ACN: 514 302 846<br>ABN: 41 652 908 237<span>EC LIC: 40917</span></div>
</header>

<section class="values">
  <div class="values-band"></div>
  <div class="value" style="left:65px">
    <div class="head">
      <svg width="62" height="62" viewBox="0 0 62 62" fill="none" stroke="#fff" stroke-width="3"><circle cx="28" cy="34" r="24"/><circle cx="28" cy="34" r="15"/><circle cx="28" cy="34" r="6" fill="#fff"/><path d="M28 34 52 10M46 8l6 2 2 6"/></svg>
      <h3>OUR VALUES</h3>
    </div>
    <p>Lorem Ipsum is simply dummy text of the printing and type setting industry.</p>
  </div>
  <div class="value featured" style="left:331px">
    <div class="head">
      <svg width="62" height="62" viewBox="0 0 62 62" fill="none" stroke="#fff" stroke-width="3"><path d="M31 4 8 12v18c0 14 10 24 23 28 13-4 23-14 23-28V12Z"/><path d="M31 4v54M8 30h46"/></svg>
      <h3>SAFETY</h3>
    </div>
    <p>Lorem Ipsum is simply dummy text of the printing and type setting industry. Text of the printing and type setting psum is simply dummy text of the printing and type setting industry</p>
  </div>
  <div class="value" style="left:607px">
    <div class="head">
      <svg width="62" height="62" viewBox="0 0 62 62" fill="none" stroke="#fff" stroke-width="3" stroke-linejoin="round"><path d="M8 28h12v28H8zM20 30l10-14 2-12c6 0 8 6 6 14h14c4 0 5 4 3 6 2 2 2 5-1 7 2 2 1 5-2 6 1 3-1 6-4 6H20"/></svg>
      <h3>QUALITY</h3>
    </div>
    <p>Lorem Ipsum is simply dummy text of the printing and type setting industry.</p>
  </div>
  <div class="value" style="left:863px">
    <div class="head">
      <svg width="70" height="62" viewBox="0 0 70 62" fill="none" stroke="#fff" stroke-width="3" stroke-linejoin="round"><path d="M4 20 14 12l10 6h10l-10 10c-3 3 2 7 6 4l8-6 16 14-12 10-6-4M66 20 56 12l-10 4M14 34l18 16M10 28l8 6M20 40l8 7"/></svg>
      <h3>RELIABILITY</h3>
    </div>
    <p>Lorem Ipsum is simply dummy text of the printing and type setting industry.</p>
  </div>
</section>

<section class="welcome">
  <h2>WELCOME TO TOLBRAN ENGINEERING</h2>
  <p class="intro">Lorem Ipsum is simply dummy text of the printing and typesetting industry. Lorem Ipsum has been the industry's standard dummy text ever since the 1500s, when an unknown printer took a galley of type and scrambled it to make a type specimen book. It has survived not only five centuries.</p>
  <div class="sectors">
    <div class="sector">
      <svg width="76" height="56" viewBox="0 0 76 56" fill="var(--orange)"><path d="M38 2 2 30h10v26h20V40h12v16h20V30h10L60 18V6h-8v6Z"/></svg>RESIDENTIAL
    </div>
    <div class="sector">
      <svg width="68" height="60" viewBox="0 0 68 60" fill="var(--orange)"><path d="M6 12h22V2h16v58H6Zm42 18h16v30H48Z"/><g fill="#efefef"><rect x="12" y="20" width="5" height="6"/><rect x="21" y="20" width="5" height="6"/><rect x="12" y="32" width="5" height="6"/><rect x="21" y="32" width="5" height="6"/><rect x="33" y="10" width="5" height="6"/><rect x="33" y="22" width="5" height="6"/><rect x="33" y="34" width="5" height="6"/><rect x="53" y="36" width="6" height="6"/><rect x="53" y="48" width="6" height="6"/></g></svg>COMMERCIAL
    </div>
    <div class="sector">
      <svg width="66" height="60" viewBox="0 0 66 60" fill="var(--orange)"><path d="M4 60V4h12v22l16-10v10l16-10v10l14-8v42Z"/><g fill="#efefef"><rect x="14" y="38" width="8" height="8"/><rect x="30" y="38" width="8" height="8"/><rect x="46" y="38" width="8" height="8"/></g></svg>INDUSTRIAL
    </div>
  </div>
  <div class="person-photo" role="img" aria-label="Photo of a smiling tradesman in a grey shirt with arms folded"></div>
</section>

<section class="about-band">
  <h2>KNOW MORE ABOUT TOLBRAN ENGINEERING</h2>
  <p>Lorem Ipsum is simply dummy text of the printing and typesetting industry. Lorem Ipsum has been the text of industry's standard dummy text ever since the 1500s</p>
  <div class="member-badge" role="img" aria-label="Industry association member badge"></div>
</section>

<section class="projects">
  <h2>RECENT PROJECT</h2>
  <article class="project" style="left:78px">
    <div class="project-photo panel-a" role="img" aria-label="Photo of wired switchboard breakers"></div>
    <div class="project-info">
      <h3>HALDEN LIFTDECK 4000</h3>
      <p class="desc">Cmmissioning and maintenance of a5 tonne Materials hoist</p>
      <dl><dt>Client</dt><dd>Corvell Lifting Co</dd><dt>Location</dt><dd>Marlow Build Group - Harbour Plaza - Dunmore City</dd></dl>
    </div>
  </article>
  <article class="project" style="left:607px">
    <div class="project-photo panel-b" role="img" aria-label="Photo of hoist control cabinet interior"></div>
    <div class="project-info">
      <h3>HALDEN LIFTDECK 4000</h3>
      <p class="desc">Cmmissioning and maintenance of a5 tonne Materials hoist</p>
      <dl><dt>Client</dt><dd>Corvell Lifting Co</dd><dt>Location</dt><dd>Marlow Build Group - Harbour Plaza - Dunmore City</dd></dl>
    </div>
  </article>
</section>

<section class="contact">
  <h2>CONTACT US</h2>
  <p class="lead">Lorem Ipsum is simply dummy text of the printing and typesetting industry. Lorem Ipsum has been the industry's standard dummy text ever since the 1500s, when an unknown printer took.</p>
  <div class="field" style="left:154px;top:2180px;top:180px;width:290px;height:52px">Name*</div>
  <div class="field" style="left:454px;top:180px;width:291px;height:52px">Email*</div>
  <div class="field" style="left:755px;top:180px;width:291px;height:52px">Phone*</div>
  <div class="field" style="left:154px;top:241px;width:892px;height:104px">Message*</div>
  <div class="submit">SUBMIT</div>
</section>

<footer class="site-footer">
  <div class="footer-brand">
    <div class="brand-dot"></div>
    <div class="name">TOLBRAN</div>
    <div class="ids">ACN: 514 302 846<br>ABN: 41 652 908 237 &nbsp; EC LIC: 40917</div>
  </div>
  <div class="footer-col" style="left:345px">
    <h4>USEFULL LINKS</h4>
    <ul class="links"><li>Home</li><li>Residential</li><li>Commercial</li><li>Industrial</li><li>About Us</li><li>Contact Us</li></ul>
  </div>
  <div class="footer-col touch" style="left:608px">
    <h4>GET IN TOUCH</h4>
    <div class="row"><svg width="16" height="20" viewBox="0 0 16 20" fill="none" stroke="#fff" stroke-width="1.6"><path d="M8 19S2 12 2 8a6 6 0 0 1 12 0c0 4-6 11-6 11Z"/><circle cx="8" cy="8" r="2"/></svg><div><strong>TOLBRAN ENGINEERING</strong><br>Lorem ipsum dolor amet simple.</div></div>
    <div class="row"><svg width="18" height="18" viewBox="0 0 18 18" fill="none" stroke="#fff" stroke-width="1.6"><path d="M4 1 1 4c0 7 6 13 13 13l3-3-4-3-2 2C8 12 6 10 5 7l2-2Z"/></svg><div>0400 000 318</div></div>
    <div class="row"><svg width="18" height="18" viewBox="0 0 18 18" fill="none" stroke="#fff" stroke-width="1.6"><rect x="2" y="7" width="14" height="7"/><path d="M5 7V2h8v5M5 12h8v5H5Z"/></svg><div>08 5550 12 34</div></div>
    <div class="row"><svg width="18" height="14" viewBox="0 0 18 14" fill="none" stroke="#fff" stroke-width="1.6"><rect x="1" y="1" width="16" height="12"/><path d="m1 1 8 7 8-7"/></svg><div>info@tolbran.net.au</div></div>
  </div>
  <div class="footer-col newsletter" style="left:874px">
    <h4>NEWSLETTER</h4>
    <p>Subscribe to stay on Tolbran Engineering updates</p>
    <div class="subscribe"><span>Enter your Email</span><i><svg width="26" height="26" viewBox="0 0 26 26" fill="none" stroke="var(--orange)" stroke-width="2" stroke-linejoin="round"><path d="M24 2 2 11l9 4 4 9Z M24 2 11 15"/></svg></i></div>
  </div>
</footer>
<div class="bottom-bar" style="position:absolute;left:0;width:1200px">© 2016 <b>Tolbran Engineering Pty Ltd</b> - All rights reserved. EC 40917</div>

</body>
</html>
```